Bright and beautiful business card for a coach

I'm a personal and business coach based in Perth, Australia. I need a business card that whilst subtle and elegant, will stand out and appeal on a table full of cards.

My business name is Tide Mentoring and the business card must represent the warmth and brightness implied in the name, without being gimmicky. It must have a warmth and appeal and be easy to read.

I prefer clean, minimalist designs.

It must align with the feel of my website and socials: https://www.tidementoring.com.au/
https://www.instagram.com/tidementoringau/
https://www.facebook.com/tidementoringau
Updates

Hi Designers Thank you so much for taking the time to submit designs. I wonder if I could have explained myself a little better. Most of the designs that have been submitted look rather formal and many have quite corporate looking embellishments on them (to my eye). I would like softer, warmer, more organic. I’m open to people playing about and being more abstract, using softer embellishments (e.g the line drawing flowers and grasses I’ve used in my socials) incorporating other colours from my palette or like the social icons in my email signature (in PDF), perhaps playing with size/oversize, playing with the bleed. Please don’t be constrained by what I’ve already done, it merely needs to compliment. I’m sorry if I’m not using the right words or have led you astray. I’m no designer, but I’ve done my website, socials, email signature etc all myself (my logo was a design contest) and I was really hoping for my business card to be something more creative than I could have made with a template. Reminder: No black cards/sides please. Thank you 😊

Target Market(s)

Individuals, most likely but not all female. Creative thinkers. Likely professionals.

Industry/Entity Type

Business & Personal Coach

Contact Information for Business Card

(Tide Mentoring Logo) Name: Maren Delsby; Title: Business & Personal Coach; Phone number: +61 (0)438 915307; Email: maren@tidementoring.com.au; Website: https://tidementoring.com.au; Social icons for Facebook, Instagram & LinkedIn: @tidementoringAU. Optional strapline: "A thinking partner to help you cut through the noise"

Font styles to use
Sans Serif

Colors
00AB8E
00BBA5
67D7C9
C6EFE9
E9F9F6
59FF00
82FF00
B8FF75
E3FFCB
F4FFEA
FFC000
F8CF3A
FAE287
FDF2CF
FEFAEE

Requirements
Must have
• Must align with feel of my website and socials. Must have a pop of #FFC000 (possibly whole of one side, or at least a block). Bright or white background. Easy to read.
Nice to have
• Possibly incorporate the sunshine/grass picture I have used in website and socials - will upload.
Should not have
• Must not be black or dark. Not impersonal or corporate looking.

```html
<!DOCTYPE html>
<html lang="en">
<head>
<meta charset="utf-8">
<title>Tide Mentoring – Business Card</title>
<link href="https://fonts.googleapis.com/css2?family=Josefin+Sans:wght@700&family=Montserrat:wght@400;500;600&display=swap" rel="stylesheet">
<style>
  :root {
    --page: #ececec;
    --card: #ffffff;
    --gold: #f2b600;
    --amber: #d98a14;
    --rust: #c0661e;
    --lime: #cfd84a;
    --ink: #5f6568;
    --photo-green: #55752a;
    --icon: #e89a1a;
  }
  * { box-sizing: border-box; margin: 0; padding: 0; }
  html, body { width: 1200px; height: 1199px; overflow: hidden; background: var(--page); }
  body { position: relative; font-family: "Montserrat", Arial, sans-serif; }

  .card {
    position: absolute;
    left: 195px;
    width: 833px;
    height: 454px;
    background: var(--card);
    box-shadow: 0 10px 24px rgba(0,0,0,.18);
    overflow: hidden;
  }
  .card--front { top: 112px; }
  .card--back { top: 646px; }

  /* Front */
  .brand {
    position: absolute;
    left: 50px; top: 196px;
    width: 350px;
    text-align: center;
    font-weight: 500;
    font-size: 33px;
    letter-spacing: 1px;
    color: var(--amber);
  }
  .divider {
    position: absolute;
    left: 433px; top: 154px;
    width: 2px; height: 141px;
    background: var(--gold);
  }
  .details { position: absolute; left: 467px; top: 150px; }
  .details__name {
    font-weight: 600;
    font-size: 33px;
    letter-spacing: 1.2px;
    color: var(--gold);
    line-height: 1;
  }
  .details__title {
    margin-top: 6px;
    font-size: 20.5px;
    color: var(--ink);
    letter-spacing: .4px;
  }
  .contacts { list-style: none; margin-top: 13px; }
  .contacts li {
    display: flex; align-items: center; gap: 7px;
    font-size: 19px;
    color: var(--ink);
    line-height: 26px;
    letter-spacing: .1px;
  }
  .contacts svg { width: 13px; height: 13px; flex: none; }

  .band-line {
    position: absolute; left: 0; right: 0; top: 390px;
    height: 6px; background: var(--lime);
  }
  .band {
    position: absolute; left: 0; right: 0; top: 396px; bottom: 0;
    background: linear-gradient(90deg, var(--rust) 0%, var(--amber) 45%, var(--gold) 85%, #f5c62a 100%);
    display: flex; align-items: center; justify-content: center; gap: 10px;
  }
  .social-mark {
    width: 25px; height: 25px;
    border-radius: 4px;
    background: #ffffff;
  }
  .band__handle {
    margin-left: 6px;
    font-size: 20px;
    color: #ffffff;
    letter-spacing: .3px;
  }

  /* Back */
  .photo {
    position: absolute; inset: 0;
    background: var(--photo-green);
  }
  .strapline {
    position: absolute; left: 0; right: 0; top: 190px;
    text-align: center;
    font-family: "Josefin Sans", "Futura", sans-serif;
    font-weight: 700;
    font-size: 33px;
    line-height: 41px;
    letter-spacing: 2.4px;
    color: #ffffff;
  }
</style>
</head>
<body>

<section class="card card--front" aria-label="Business card front">
  <div class="brand">Tide Mentoring</div>
  <div class="divider"></div>
  <div class="details">
    <h1 class="details__name">MAREN DELSBY</h1>
    <p class="details__title">Business &amp; Personal Coach</p>
    <ul class="contacts">
      <li>
        <svg viewBox="0 0 16 16" aria-hidden="true"><path d="M4 1.5 6.3 4 5 5.8c.9 2 2.6 3.8 4.7 4.8L11.4 9.3 14 11.6 12.6 14C7 13.6 2.2 8.8 1.8 3.1Z" fill="none" stroke="var(--icon)" stroke-width="1.6" stroke-linejoin="round"/></svg>
        +61 (0)438 915307
      </li>
      <li>
        <svg viewBox="0 0 16 16" aria-hidden="true"><rect x="1" y="3" width="14" height="10" fill="none" stroke="var(--icon)" stroke-width="1.5"/><path d="M1 3.5 8 9l7-5.5" fill="none" stroke="var(--icon)" stroke-width="1.5"/></svg>
        maren@tidementoring.com.au
      </li>
      <li>
        <svg viewBox="0 0 16 16" aria-hidden="true"><circle cx="8" cy="8" r="6.5" fill="none" stroke="var(--icon)" stroke-width="1.3"/><ellipse cx="8" cy="8" rx="2.8" ry="6.5" fill="none" stroke="var(--icon)" stroke-width="1.1"/><path d="M1.5 8h13M2.5 5h11M2.5 11h11" stroke="var(--icon)" stroke-width="1"/></svg>
        www.tidementoring.com.au
      </li>
    </ul>
  </div>
  <div class="band-line"></div>
  <div class="band">
    <span class="social-mark" aria-hidden="true"></span>
    <span class="social-mark" aria-hidden="true"></span>
    <span class="social-mark" aria-hidden="true"></span>
    <span class="band__handle">@tidementoringau</span>
  </div>
</section>

<section class="card card--back" aria-label="Business card back">
  <div class="photo" role="img" aria-label="Photograph area: close-up of green grass with sunlight through trees"></div>
  <p class="strapline">A THINKING PARTNER TO HELP<br>YOU CUT THROUGH THE NOISE</p>
</section>

</body>
</html>
```